Corvale Homes

To produce a business card design for our newly established house building and development company, We have had a logo design done please see attached, our slogan is "building your home sweet home"
Contact Information for Business Card
Adress on card needs to Read - 58 Elmsworth Lane, Kettering, Northamptonshire NN16 4QT. Director name Dean Vascotti
Requirements
Must have
- Web adress is www.corvale-homes.co.uk
- Email address is info@corvale-homes.co.uk
- phone number 07700 900417

```html
<!DOCTYPE html>
<html lang="en">
<head>
<meta charset="utf-8">
<title>Corvale Homes — Business Card</title>
<link rel="stylesheet" href="https://fonts.googleapis.com/css2?family=Lato:wght@400;700&display=swap">
<style>
  :root {
    --backdrop: #e9ecef;
    --brand-green: #8dc63f;
    --card-white: #ffffff;
    --ink-grey: #6d6e70;
    --rule-grey: #8a8b8d;
  }
  * { box-sizing: border-box; margin: 0; padding: 0; }
  html, body {
    width: 1200px;
    height: 1000px;
    overflow: hidden;
    background: var(--backdrop);
    font-family: "Lato", Arial, sans-serif;
  }
  .sheet {
    position: relative;
    width: 1200px;
    height: 1000px;
  }
  .card {
    position: absolute;
    left: 220px;
    width: 760px;
    height: 434px;
    box-shadow: 0 6px 20px rgba(0, 0, 0, 0.15);
  }
  .card--front {
    top: 46px;
    background: var(--brand-green);
    display: flex;
    align-items: center;
    justify-content: center;
  }
  .card--back {
    top: 520px;
    background: var(--card-white);
    color: var(--ink-grey);
  }
  .wordmark {
    font-weight: 700;
    white-space: nowrap;
  }
  .card--front .wordmark {
    color: var(--card-white);
    font-size: 68px;
    letter-spacing: 2px;
    text-transform: uppercase;
  }
  .card--back .wordmark {
    position: absolute;
    right: 36px;
    top: 62px;
    color: var(--brand-green);
    font-size: 40px;
  }
  .holder-name {
    position: absolute;
    left: 34px;
    top: 78px;
    font-size: 37px;
    font-weight: 400;
  }
  .holder-role {
    position: absolute;
    left: 35px;
    top: 126px;
    font-size: 22px;
  }
  .rule {
    position: absolute;
    left: 34px;
    right: 36px;
    height: 2px;
    background: var(--rule-grey);
  }
  .rule--top { top: 211px; }
  .rule--bottom { top: 342px; }
  .contact-list {
    position: absolute;
    left: 34px;
    top: 238px;
    list-style: none;
    font-size: 27px;
  }
  .contact-list li {
    display: flex;
    align-items: center;
    height: 36px;
  }
  .contact-icon {
    width: 20px;
    height: 20px;
    margin-right: 18px;
    fill: var(--ink-grey);
  }
  .address {
    position: absolute;
    right: 36px;
    top: 218px;
    font-style: normal;
    font-size: 19.5px;
    line-height: 28.5px;
    text-align: right;
  }
  .website {
    position: absolute;
    right: 40px;
    top: 366px;
    font-size: 20px;
  }
</style>
</head>
<body>
<main class="sheet">
  <section class="card card--front" aria-label="Business card front">
    <span class="wordmark">Corvale Homes</span>
  </section>

  <section class="card card--back" aria-label="Business card back">
    <h1 class="holder-name">Dean Vascotti</h1>
    <p class="holder-role">Director</p>
    <span class="wordmark">Corvale Homes</span>

    <div class="rule rule--top"></div>

    <ul class="contact-list">
      <li>
        <svg class="contact-icon" viewBox="0 0 24 24" aria-hidden="true">
          <path d="M6.6 10.8c1.4 2.8 3.8 5.1 6.6 6.6l2.2-2.2c.3-.3.7-.4 1-.2 1.1.4 2.3.6 3.6.6.6 0 1 .4 1 1V20c0 .6-.4 1-1 1C10.6 21 3 13.4 3 4c0-.6.4-1 1-1h3.5c.6 0 1 .4 1 1 0 1.3.2 2.5.6 3.6.1.3 0 .7-.2 1L6.6 10.8z"/>
        </svg>
        <span>07700 900417</span>
      </li>
      <li>
        <svg class="contact-icon" viewBox="0 0 24 24" aria-hidden="true">
          <path d="M2 5h20v14H2z M3.5 6.5v.4L12 12.5l8.5-5.6v-.4z" fill-rule="evenodd"/>
        </svg>
        <span>info@corvale-homes.co.uk</span>
      </li>
    </ul>

    <address class="address">
      58 Elmsworth Lane,<br>
      Kettering,<br>
      Northamptonshire<br>
      NN16 4QT
    </address>

    <div class="rule rule--bottom"></div>

    <p class="website">www.corvale-homes.co.uk</p>
  </section>
</main>
</body>
</html>
```